Website development

Looking for a simple website, containing circa 10-15 pages of brochure-ware content for our new Cafe and Farm Shop venture.

We have a logo, designed through this site, which we think is really strong.

The Cafe and Farm Shop are all about locally sourced, high quality food served in a stunning rural location by happy, friendly staff. Great quality food and drink at sensible prices.

Initially the website needs to contain 10 or so pages of content, which ideally we would like to manage on-going (perhaps not every page, but as many pages as the budget will allow). We want to make sure that the website stays fresh and current and so we want a basic CMS to keep the text areas updated.

We would also like a simple data capture page, so that we can start to generate a database of email addresses for our on-going marketing efforts. Any thoughts around a basic CRM tool gratefully received.

The creative brief can take some inspiration from the logo, but should be bright, clean, welcoming and engaging. Not too over-bearing with colours or content. Fun, easy and interesting to use with all the text and image information clearly displayed.

We don't currently have any imagery beyond the logo, and would like to use as much free stock photography and imagery as possible. If needs be we can take some good quality pictures and provide them.

We're in the process of purchasing the URL(s) at present and will supply them in due course, but they will be based around the trading name.

If you have any more questions please do not hesitate to contact me.

Many thanks
Owen

Industry/Entity Type

Cafe

```html
<!DOCTYPE html>
<html lang="en">
<head>
<meta charset="utf-8">
<title>The Willow Barn – Cafe and Farm Shop</title>
<link rel="stylesheet" href="https://fonts.googleapis.com/css2?family=Mulish:wght@400;600;700&display=swap">
<style>
:root{
  --teal-bg:#00b0ae;
  --teal-text:#12a9a6;
  --slate:#3a676b;
  --leaf:#5a9a6a;
  --forest:#3f5c3f;
  --rust:#8a3a18;
  --white:#ffffff;
  --body-text:#4d6a55;
}
*{margin:0;padding:0;box-sizing:border-box}
html,body{width:1122px;height:1200px;overflow:hidden}
body{background:var(--teal-bg);font-family:"Mulish",sans-serif;position:relative}
.page{position:absolute;left:94px;top:0;width:935px;height:1130px;background:var(--white)}
.brand{position:absolute;left:28px;top:62px;display:flex;align-items:center;gap:10px}
.brand-dot{width:18px;height:18px;border-radius:50%;background:var(--leaf)}
.brand-name{font-size:30px;font-weight:700;color:var(--forest);line-height:1}
.brand-tag{position:absolute;left:34px;top:130px;font-size:12px;font-weight:700;letter-spacing:4px;color:var(--slate);text-transform:uppercase}
.main-nav{position:absolute;left:0;top:206px;width:935px;height:28px;background:var(--slate);display:flex;padding-left:62px;gap:0}
.main-nav a{color:var(--white);text-decoration:none;font-size:14px;line-height:28px;margin-right:66px}
.hero-frame{position:absolute;left:0;top:234px}
.hero-photo{position:absolute;left:54px;top:242px;width:826px;height:342px;background:linear-gradient(90deg,#c9736c 0%,#b86a5c 45%,#8fa9c6 55%,#a9bcd2 100%)}
.welcome{position:absolute;left:43px;top:636px;width:400px}
.welcome h1{font-size:16px;font-weight:400;color:var(--teal-text);line-height:20px}
.welcome h2{font-size:12.5px;font-weight:700;color:var(--forest);line-height:16px;margin-top:4px}
.welcome time{display:block;font-size:9.5px;font-weight:700;color:var(--rust);margin-top:3px}
.welcome p{font-size:12.5px;color:var(--body-text);line-height:15.5px;margin-top:20px}
.promo{position:absolute;left:531px;top:640px;width:358px;height:178px;background:linear-gradient(135deg,#f6c9c4 0%,#f2b6b0 60%,#f7dc5a 100%)}
.gallery{position:absolute;top:863px;height:98px;width:256px}
.g1{left:43px;background:linear-gradient(135deg,#7a4a30,#d8c6a8)}
.g2{left:337px;background:linear-gradient(135deg,#5a3a3a,#3f9a96)}
.g3{left:631px;background:linear-gradient(135deg,#5a2c22,#c0b0a0)}
.site-footer{position:absolute;left:94px;top:1007px;width:935px;height:123px;background:var(--slate)}
.footer-col{position:absolute;top:22px}
.footer-col h3{font-size:14.5px;font-weight:600;color:var(--white);margin-bottom:5px}
.footer-col a{display:block;font-size:10.5px;color:var(--teal-text);text-decoration:none;line-height:13.5px}
.fc1{left:43px}.fc2{left:281px}.fc3{left:498px}
.footer-divider{position:absolute;top:22px;width:1px;height:65px;background:var(--teal-text)}
.d1{left:240px}.d2{left:458px}
.copyright{position:absolute;left:0;top:1137px;width:1122px;text-align:center;font-size:12.5px;font-weight:700;color:var(--white)}
</style>
</head>
<body>
<div class="page">
  <div class="brand"><span class="brand-dot"></span><span class="brand-name">The Willow Barn</span></div>
  <div class="brand-tag">Cafe and Farm Shop</div>
  <nav class="main-nav">
    <a href="#">Home</a><a href="#">Products</a><a href="#">Services</a><a href="#">News</a><a href="#">Contact us</a>
  </nav>
  <svg class="hero-frame" width="935" height="360" viewBox="0 0 935 360">
    <polygon points="17,0 918,0 890,360 45,360" fill="var(--leaf)"/>
  </svg>
  <div class="hero-photo" role="img" aria-label="Photo of a cafe terrace with white parasols, wooden planters and pastel building facades"></div>
  <section class="welcome">
    <h1>Welcome to ligula porta felis euismod semper. Fusce dapibus, tellus ac cursus commodo, tortor</h1>
    <h2>Vestibulum id ligula porta felis euismod semper. Fusce dapibus, tellus ac cursus commodo,</h2>
    <time>Friday 15th, April 04:25 PM</time>
    <p>amet risus. Vivamus sagittis id ligula porta felis euismod semper. Etiam porta sem malesuada magna mollis euismod. tortor mauris condimentum nibh, ut fermentum massa justo sit amet risus. Vivamus sagittis id ligula porta felis euismod semper. Etiam porta sem malesuada magna mollis euismod.</p>
  </section>
  <div class="promo" role="img" aria-label="Promotional banner for chicken fillets, ten for ten pounds, with a buy now button"></div>
  <div class="gallery g1" role="img" aria-label="Photo of two latte art coffees with coffee beans"></div>
  <div class="gallery g2" role="img" aria-label="Photo of colourful cafe tables and chairs"></div>
  <div class="gallery g3" role="img" aria-label="Photo of a coffee counter with a chalk menu board"></div>
</div>
<footer class="site-footer">
  <div class="footer-col fc1"><h3>Products Category</h3><a href="#">Mollis Parturient</a><a href="#">ut fermentum massa</a><a href="#">um massa</a></div>
  <span class="footer-divider d1"></span>
  <div class="footer-col fc2"><h3>Services</h3><a href="#">Mollis Parturient</a><a href="#">ut fermentum massa</a></div>
  <span class="footer-divider d2"></span>
  <div class="footer-col fc3"><h3>Our Shop</h3><a href="#">Mollis Parturient</a><a href="#">ut fermentum massa</a></div>
</footer>
<div class="copyright">all right reserved © 2013</div>
</body>
</html>
```